Quillfern Nightclub Flyer (Updated)

Flyer for facebook, square is fine, or rectangular. Here is the text:
QUILLFERN
Nightclub + Lounge
presents

SPLIT DECK WEDNESDAY
Nov 29 2018

CLUB FLOOR:
GORDY B2B RALPH
THEODORE BRUSKVIK

LOUNGE:
OTIS B2B HALF TIDE
COPPER FENWICK

Powered by HALVERN Acoustics
4716 Larchmere Avenue 21+ 9pm-2am
quillfernvenue-example.com for VIP booth inquiries

Target Market(s)

Nightclub

Industry/Entity Type

Night Club

Font styles to use
Sans Serif

Colors

Designer to choose colors to be used in the design.

Requirements
Must have
• All the text listed, and plz keep the theme of the attached files. We want to stay consistent with the Quillfern brand
Nice to have
• Try to stay with the theme from the attachments
Should not have
• Dont' stray to far from the general theme we have from the attachments

```html
<!DOCTYPE html>
<html lang="en">
<head>
<meta charset="utf-8">
<title>Quillfern Nightclub + Lounge — Split Deck Wednesday</title>
<link rel="stylesheet" href="https://fonts.googleapis.com/css2?family=Lato:wght@400;700;900&family=Roboto+Condensed:wght@400&display=swap">
<style>
  :root {
    --brand-red: #e3101c;
    --ink: #0d0d0d;
    --white: #ffffff;
    --grey-rule: #555555;
    --top-brown: #5a4028;
    --top-teal: #2f8f94;
    --band-red: #f0103a;
    --band-pink: #f13fb0;
    --band-light: #f7b8ef;
    --low-teal: #1fa7b8;
    --low-pale: #eaf7fa;
    --low-violet: #a46ad9;
  }
  * { margin: 0; padding: 0; box-sizing: border-box; }
  html, body { width: 1200px; height: 800px; overflow: hidden; background: var(--white); }
  .flyer {
    position: relative;
    width: 1200px;
    height: 800px;
    overflow: hidden;
    font-family: "Lato", Arial, sans-serif;
  }
  .bg { position: absolute; left: 0; width: 1200px; }
  .bg-top {
    top: 0; height: 270px;
    background: linear-gradient(180deg, var(--top-brown) 0%, #3f6a60 35%, var(--top-teal) 100%);
  }
  .bg-band {
    top: 270px; height: 214px;
    background: radial-gradient(ellipse 420px 200px at 50% 70%, var(--band-light) 0%, var(--band-pink) 55%, var(--band-red) 100%);
  }
  .bg-low {
    top: 484px; height: 316px;
    background: radial-gradient(ellipse 520px 300px at 50% 75%, var(--white) 0%, var(--low-pale) 30%, transparent 70%),
                linear-gradient(90deg, var(--low-teal) 0%, #6cc6d3 45%, #b596e6 75%, var(--low-violet) 100%);
  }
  .text { position: absolute; white-space: nowrap; }
  .center { left: 0; width: 1200px; text-align: center; }

  .venue-name {
    top: 34px;
    font-weight: 900;
    font-size: 92px;
    letter-spacing: 6px;
    color: var(--brand-red);
    line-height: 1;
  }
  .venue-tagline {
    top: 166px;
    font-weight: 700;
    font-size: 35px;
    letter-spacing: 6px;
    color: var(--white);
  }
  .presents {
    top: 224px;
    font-weight: 700;
    font-size: 19px;
    letter-spacing: 9px;
    color: var(--white);
  }

  .room { position: absolute; top: 312px; color: var(--ink); }
  .room-lounge { right: 772px; text-align: right; }
  .room-club { left: 746px; text-align: left; }
  .room-title {
    font-weight: 700;
    font-size: 36px;
    line-height: 48px;
  }
  .room-lineup {
    font-family: "Roboto Condensed", "Arial Narrow", sans-serif;
    font-size: 38px;
    line-height: 48px;
    white-space: nowrap;
  }

  .centre-mark { position: absolute; left: 480px; top: 296px; width: 240px; height: 170px; }
  .centre-mark-name {
    position: absolute; left: 0; top: 118px; width: 240px;
    text-align: center;
    font-weight: 700;
    font-size: 30px;
    letter-spacing: 1px;
    color: var(--brand-red);
  }

  .night-title {
    top: 500px;
    font-weight: 700;
    font-size: 58px;
    color: var(--ink);
    line-height: 1;
  }
  .night-day {
    top: 566px;
    font-weight: 400;
    font-size: 50px;
    color: var(--ink);
    line-height: 1;
  }
  .night-date {
    top: 618px;
    font-weight: 400;
    font-size: 32px;
    letter-spacing: 5px;
    color: var(--ink);
  }

  .sound-partner {
    top: 690px;
    font-weight: 700;
    font-size: 25px;
    letter-spacing: 1px;
    color: var(--brand-red);
  }
  .vip-info {
    position: absolute; left: 323px; top: 730px;
    font-size: 18px; line-height: 24px;
    color: var(--ink);
    letter-spacing: 0.5px;
  }
  .info-divider {
    position: absolute; left: 598px; top: 740px;
    width: 3px; height: 44px;
    background: var(--grey-rule);
  }
  .address {
    position: absolute; left: 624px; top: 741px;
    font-size: 18px;
    color: var(--ink);
    letter-spacing: 0.5px;
  }
</style>
</head>
<body>
  <main class="flyer">
    <div class="bg bg-top" role="img" aria-label="Dark teal backdrop with soft bokeh light dots"></div>
    <div class="bg bg-band" role="img" aria-label="Glowing pink and magenta band with sparkling light dots"></div>
    <div class="bg bg-low" role="img" aria-label="Teal, white and violet glow with bokeh light dots"></div>

    <h1 class="text center venue-name">QUILLFERN</h1>
    <p class="text center venue-tagline">Nightclub+Lounge</p>
    <p class="text center presents">presents</p>

    <section class="room room-lounge">
      <h2 class="room-title">LOUNGE:</h2>
      <p class="room-lineup">OTIS B2B HALF TIDE</p>
      <p class="room-lineup">COPPER FENWICK</p>
    </section>

    <div class="centre-mark">
      <svg width="240" height="120" viewBox="0 0 240 120" aria-hidden="true">
        <circle cx="120" cy="56" r="36" fill="var(--brand-red)"/>
      </svg>
      <p class="centre-mark-name">QUILLFERN</p>
    </div>

    <section class="room room-club">
      <h2 class="room-title">CLUB FLOOR:</h2>
      <p class="room-lineup">GORDY B2B RALPH</p>
      <p class="room-lineup">THEODORE BRUSKVIK</p>
    </section>

    <h2 class="text center night-title">SPLIT DECK</h2>
    <p class="text center night-day">WEDNESDAY</p>
    <p class="text center night-date">Nov 29 2018</p>

    <p class="text center sound-partner">Powered by HALVERN Acoustics</p>
    <p class="vip-info">quillfernvenue-example.com<br>for VIP booth inquiries</p>
    <div class="info-divider"></div>
    <p class="address">4716 Larchmere Avenue, 21+ 9pm-2am</p>
  </main>
</body>
</html>
```